1923 Basins & Spouts Business Card

I'm wanting to get a business card designed. Our business is 1923 Basins & Spouts
Details for the card:

1923 Basins & Spouts
Name: Gareth Vostle
Email: gareth@1923basinsandspouts.com.au
Website: www.1923basinsandspouts.com.au
Mobile: 0439 602 158
Phone: 02 5550 1843

Font of Basins & Spouts is called Snell Roundhand. Not sue what font logo text is.

I'm thinking two sided but it doesn't have to be.

```html
<!DOCTYPE html>
<html lang="en">
<head>
<meta charset="utf-8">
<title>1923 Basins &amp; Spouts – Business Card</title>
<link rel="stylesheet" href="https://fonts.googleapis.com/css2?family=Pinyon+Script&family=Open+Sans:wght@400&family=Arimo:wght@400&display=swap">
<style>
  :root {
    --page: #e9e9ea;
    --card: #ffffff;
    --ink: #111111;
    --rule: #3a3a3a;
    --ornament-a: #f3f3f3;
    --ornament-b: #fbfbfb;
    --icon: #1a1a1a;
  }
  * { box-sizing: border-box; margin: 0; padding: 0; }
  html, body { width: 1200px; height: 880px; overflow: hidden; }
  body {
    background: var(--page);
    position: relative;
    font-family: "Open Sans", sans-serif;
    color: var(--ink);
  }
  .card {
    position: absolute;
    left: 280px;
    width: 640px;
    height: 366px;
    background: var(--card);
    border-radius: 18px;
    box-shadow: 0 6px 22px rgba(0,0,0,0.12);
    overflow: hidden;
  }
  .card--front { top: 58px; }
  .card--back { top: 456px; }

  .ornament {
    position: absolute;
    border-radius: 50%;
    background: radial-gradient(ellipse at center, var(--ornament-a) 0%, var(--ornament-b) 60%, rgba(255,255,255,0) 75%);
  }
  .card--front .ornament { left: 120px; top: 10px; width: 440px; height: 340px; }
  .card--back .ornament { left: -40px; top: 20px; width: 360px; height: 320px; }

  /* brand name: one font, one weight, one colour */
  .brand {
    display: flex;
    align-items: center;
    gap: 12px;
  }
  .brand__dot {
    width: 14px; height: 14px;
    border-radius: 50%;
    background: var(--ink);
    flex: none;
  }
  .brand__name {
    font-family: "Open Sans", sans-serif;
    font-weight: 400;
    color: var(--ink);
    line-height: 1.1;
    white-space: nowrap;
  }

  /* front */
  .front-lockup {
    position: absolute;
    left: 110px;
    top: 142px;
  }
  .front-lockup .brand__name { font-size: 34px; letter-spacing: 0.3px; }
  .front-lockup__tagline {
    font-size: 13px;
    letter-spacing: 0.2px;
    margin-top: 8px;
    margin-left: 26px;
  }

  /* back */
  .person {
    position: absolute;
    left: 60px;
    top: 112px;
    font-family: "Pinyon Script", cursive;
    font-size: 44px;
    white-space: nowrap;
  }
  .back-brand {
    position: absolute;
    left: 350px;
    top: 96px;
  }
  .back-brand .brand__name { font-size: 25px; }
  .rule { position: absolute; height: 1.5px; background: var(--rule); }
  .rule--top { left: 338px; width: 270px; top: 162px; }
  .rule--bottom { left: 40px; width: 270px; top: 268px; }

  .contact-list {
    position: absolute;
    list-style: none;
    font-family: "Arimo", sans-serif;
    font-size: 15.5px;
    letter-spacing: 0.3px;
  }
  .contact-list--online { left: 350px; top: 184px; }
  .contact-list--phone { left: 50px; top: 282px; }
  .contact-list li {
    display: flex;
    align-items: center;
    gap: 9px;
    height: 26px;
    white-space: nowrap;
  }
  .contact-list--online li { font-size: 13px; letter-spacing: 0.1px; }
  .icon { width: 18px; height: 18px; flex: none; }
</style>
</head>
<body>

<section class="card card--front" aria-label="Card front">
  <div class="ornament" role="img" aria-label="Faint decorative scrollwork background"></div>
  <div class="front-lockup">
    <div class="brand">
      <span class="brand__dot"></span>
      <span class="brand__name">1923 Basins &amp; Spouts</span>
    </div>
    <div class="front-lockup__tagline">Crafted fixtures blending classic style with daily use</div>
  </div>
</section>

<section class="card card--back" aria-label="Card back">
  <div class="ornament" role="img" aria-label="Faint decorative scrollwork background"></div>

  <div class="person">Gareth Vostle</div>

  <div class="brand back-brand">
    <span class="brand__dot"></span>
    <span class="brand__name">1923 Basins &amp; Spouts</span>
  </div>

  <div class="rule rule--top"></div>
  <ul class="contact-list contact-list--online">
    <li>
      <svg class="icon" viewBox="0 0 18 18" aria-hidden="true"><circle cx="9" cy="9" r="9" fill="var(--icon)"/><rect x="4.5" y="5.8" width="9" height="6.4" fill="none" stroke="#fff" stroke-width="1.1"/><path d="M4.5 5.8 9 9.6l4.5-3.8" fill="none" stroke="#fff" stroke-width="1.1"/></svg>
      gareth@1923basinsandspouts.com.au
    </li>
    <li>
      <svg class="icon" viewBox="0 0 18 18" aria-hidden="true"><circle cx="9" cy="9" r="9" fill="var(--icon)"/><circle cx="9" cy="9" r="5" fill="none" stroke="#fff" stroke-width="1"/><ellipse cx="9" cy="9" rx="2.2" ry="5" fill="none" stroke="#fff" stroke-width="1"/><path d="M4 9h10" stroke="#fff" stroke-width="1"/></svg>
      www.1923basinsandspouts.com.au
    </li>
  </ul>

  <div class="rule rule--bottom"></div>
  <ul class="contact-list contact-list--phone">
    <li>
      <svg class="icon" viewBox="0 0 18 18" aria-hidden="true"><circle cx="9" cy="9" r="9" fill="var(--icon)"/><path d="M6 5c.6-.4 1.2-.3 1.5.3l.7 1.4c.2.4 0 .8-.3 1l-.5.4c.5 1.1 1.3 1.9 2.4 2.4l.4-.5c.3-.3.7-.4 1-.2l1.4.7c.6.3.7.9.3 1.5-.6.9-1.600 1.1-2.6.6C8.2 11.7 6.3 9.8 5.4 8 5 7 5.1 5.6 6 5z" fill="#fff"/></svg>
      0439 602 158
    </li>
    <li>
      <svg class="icon" viewBox="0 0 18 18" aria-hidden="true"><circle cx="9" cy="9" r="9" fill="var(--icon)"/><rect x="5.5" y="4.5" width="7" height="9" rx="1" fill="none" stroke="#fff" stroke-width="1.1"/><path d="M7 11.5h4" stroke="#fff" stroke-width="1.1"/></svg>
      02 5550 1843
    </li>
  </ul>
</section>

</body>
</html>
```